Professional CPA firm wants card to tell our clients why employees are wearing jeans today

We are a professional CPA firm and want to allow our employees the choice to wear jeans instead of professional attire for the day at the cost of contributing $2.00 to a collection jar for a local charity - at the end of a six month period the firm will donate the money collected from the employees to the local charity

HI - We are located in a town called Auburn - instead of the copy saying "local charity", I'd like it to reference that it will go to an "Auburn centered charity"

thanks!                                   

It Professional

```html
<!DOCTYPE html>
<html lang="en">
<head>
<meta charset="utf-8">
<title>Wear Your Jeans – Charity Card</title>
<link rel="stylesheet" href="https://fonts.googleapis.com/css2?family=Ultra&family=Sancreek&family=Rokkitt:wght@700&family=Open+Sans:wght@400&display=swap">
<style>
  :root {
    --page: #ffffff;
    --denim-light: #4d6a92;
    --denim-dark: #2c4264;
    --tag-dark: #4e3210;
    --tag-mid: #7a5a2c;
    --tag-tan: #b39a68;
    --tag-paper: #efece4;
    --navy: #1c2f6c;
    --white: #ffffff;
  }
  * { margin: 0; padding: 0; box-sizing: border-box; }
  html, body {
    width: 1200px; height: 1000px; overflow: hidden;
    background: var(--page);
  }
  .card {
    position: absolute; left: 346px; top: 95px;
    width: 519px; height: 767px; overflow: hidden;
  }
  .denim-photo {
    position: absolute; inset: 0;
    background: linear-gradient(160deg, var(--denim-light) 0%, var(--denim-dark) 55%, var(--denim-light) 100%);
  }
  .tag {
    position: absolute; left: 92px; top: 62px;
    width: 360px; height: 700px;
    transform: rotate(-3.2deg); transform-origin: top left;
    border-radius: 6px; overflow: hidden;
    background: linear-gradient(180deg, var(--tag-dark) 0%, var(--tag-mid) 34%, var(--tag-tan) 46%, var(--tag-tan) 100%);
    text-align: center;
    display: flex; flex-direction: column;
  }
  .headline {
    font-family: "Ultra", serif; font-weight: 400; color: var(--white);
    line-height: 0.9; padding-top: 32px;
    text-shadow: 2px 3px 4px rgba(0,0,0,0.55);
  }
  .headline .small { display: block; font-size: 34px; }
  .headline .large { display: block; font-size: 60px; }
  .appeal { color: var(--navy); margin-top: 34px; }
  .appeal .contribute { font-family: "Rokkitt", serif; font-weight: 700; font-size: 26px; letter-spacing: 1px; line-height: 1.1; }
  .appeal .amount { font-family: "Sancreek", serif; font-size: 94px; line-height: 1; }
  .appeal .terms {
    font-family: "Rokkitt", serif; font-weight: 700; font-size: 18px;
    line-height: 1.1; margin-top: 4px; white-space: nowrap;
  }
  .details {
    font-family: "Rokkitt", serif; font-weight: 700; font-size: 15px;
    color: var(--white); line-height: 1.1; margin-top: 14px; white-space: nowrap;
  }
  .spacer { flex: 1 1 auto; }
  .firm {
    flex: 0 0 86px;
    background: var(--tag-paper); color: var(--navy);
    padding-top: 18px;
  }
  .firm .name { font-family: "Rokkitt", serif; font-weight: 700; font-size: 28px; line-height: 1; }
  .firm .type { font-family: "Open Sans", sans-serif; font-size: 12px; letter-spacing: 0.5px; margin-top: 4px; }
</style>
</head>
<body>
  <div class="card">
    <div class="denim-photo" role="img" aria-label="Close-up photo of the back pocket of blue denim jeans with orange stitching"></div>
    <div class="tag">
      <h1 class="headline">
        <span class="small">WEAR YOUR</span>
        <span class="large">JEANS</span>
        <span class="small">AND HELP</span>
        <span class="large">CHANGE</span>
        <span class="large">LIVES</span>
      </h1>
      <div class="appeal">
        <div class="contribute">CONTRIBUTE</div>
        <div class="amount">$2.00</div>
        <p class="terms">AND WEAR YOUR JEANS INSTEAD OF<br>PROFESSIONAL ATTIRE<br>FOR THE DAY</p>
      </div>
      <p class="details">AT THE END OF A SIX MONTH PERIOD<br>THE FIRM WILL DONATE THE MONEY<br>COLLECTED FROM THE EMPLOYEES TO AN<br>AUBURN CHARITY</p>
      <div class="spacer"></div>
      <div class="firm">
        <div class="name">Hollis, Marsh &amp; Vane</div>
        <div class="type">CERTIFIED PUBLIC ACCOUNTANTS, INC</div>
      </div>
    </div>
  </div>
</body>
</html>
```